Zielgruppe
Express-Transporte / Sonderfahrten / Speditionsdienstleistungen
Aufgabenstellung
- - - WORDPRESS Design gesucht - - -
seriosität für b2b ; primär werden Kastensprinter und Planensprinter eingesetzt , nur Stock Bilder verwenden die ohne ein Abo gekauft werden können ; die präsentation soll das unternehmen gross aussehen lassen, ((bitte die Powerpoint lediglich für die übersicht der dienstleistungen verwenden.)) Es sollte mit dem Firmenlogo harmonieren. Es wird nach einem komplett neuen Design gesucht. Gerne die Farbtöne des Logo verwenden. Es wird nach einer Onepage gesucht mit einem modernen Design für Wordpress.
Ähnlich wie die derzeitige website https://welmacor-logistik.example jedoch komplett neu.
Weder mit Website Design noch mit dem der powerpoint bin ich stand jetzt zufrieden.
Ich suche hier nach etwas komplett neuem.
Bereits beantwortete fragen:
1.) Zweck: Vorstellung vom Unternehmen und Dienstleistungen
2.) Zielgruppe: Nekunden / Bestandskunden / generelle übersicht der Dienstleistungen
3.) Auf die Landingpage sollen die im grunde alle Leistungen die wir anbieten und zusätzlich noch einen Text dazu quasi ein über uns Text.
4.) Die Bilder können zur Verfügung gestellt werden. Gerne kann hier jedoch auch via Pixalumen bsp. 'bessere' Bilder verwendet werden
5.) Gerne darf die Website heller sein ; keine direkte vorstellung der Farben. Ggf. ähnlich dem derzeitgen Logo in die richtung Rot/Grau .. allerdings gerne hier auch freie entscheidung / kreativität
6.) mir gefallen die Website xyz und xyz gut (link bitte anfragen)
Bei fragen bitte melden.
Erreichbar Montag - Freitag 08.00 - 17.00h

```html
<!DOCTYPE html>
<html lang="de">
<head>
<meta charset="utf-8">
<title>Welmacor – Transport | Spedition</title>
<link href="https://fonts.googleapis.com/css2?family=Montserrat:wght@400;500;600;700&display=swap" rel="stylesheet">
<style>
:root{
  --red:#d52229;
  --red-dark:#b3181e;
  --ink:#2a2a2a;
  --dark:#221d1a;
  --footer-bar:#2b2b2b;
  --white:#ffffff;
  --muted:#555;
}
*{margin:0;padding:0;box-sizing:border-box}
html,body{width:1200px;height:3869px;overflow:hidden}
body{font-family:"Montserrat",Arial,sans-serif;color:var(--ink);position:relative;background:#fff}
section,header,footer{position:absolute;left:0;width:1200px}
.abs{position:absolute}

/* hero */
.hero{top:0;height:803px;overflow:hidden}
.hero-photo{position:absolute;inset:0;background:
  radial-gradient(ellipse at 60% 55%,#6b6b68 0%,#4a4a48 35%,#2b2b2a 70%,#1c1c1c 100%)}
.hero-shade{position:absolute;inset:0;background:rgba(0,0,0,.35)}
.brand{position:absolute;left:90px;top:20px;color:var(--white);font-weight:500;font-size:40px;letter-spacing:1px;display:flex;align-items:center;gap:12px}
.brand-mark{width:22px;height:22px;background:var(--red)}
.nav{position:absolute;right:74px;top:49px;display:flex;gap:38px}
.nav a{color:var(--white);text-decoration:none;font-weight:700;font-size:14px;letter-spacing:.5px}
.hero-title{position:absolute;top:295px;width:1200px;text-align:center;color:var(--red);font-size:90px;font-weight:400;letter-spacing:4px;line-height:1}
.hero-sub{position:absolute;top:390px;width:1200px;text-align:center;color:#eee;font-size:46px;font-weight:400;letter-spacing:2px;line-height:1}
.hero-tag{position:absolute;top:454px;width:1200px;text-align:center;color:#eee;font-size:22px;font-weight:400}
.hero-btn{position:absolute;left:504px;top:552px;width:218px;height:61px;border:2px solid var(--white);color:var(--white);font-weight:700;font-size:20px;display:flex;align-items:center;justify-content:center;letter-spacing:.5px}

/* about */
.about{top:803px;height:597px;overflow:hidden}
.about-photo{position:absolute;inset:0;background:linear-gradient(90deg,#6d6259 0%,#9a9893 40%,#d8d8d6 65%,#e9e9e7 85%,#8b8f92 100%)}
.card{position:absolute;background:var(--white)}
.about .card{left:95px;top:68px;width:694px;height:478px;padding:0 40px}
.card h2{color:var(--red);font-weight:400;font-size:43px;letter-spacing:.5px}
.about h2{margin-top:28px;margin-left:-5px}
.card p{font-size:17.5px;line-height:26px;color:var(--muted)}
.about p{margin-top:18px;width:614px}

/* services */
.services{top:1400px;height:640px;background:var(--red)}
.section-title{position:absolute;width:1200px;text-align:center;font-weight:400;font-size:46px;line-height:54px;letter-spacing:1px}
.services .section-title{top:48px;color:var(--white)}
.svc{position:absolute;top:201px;width:321px;height:321px;background:var(--red-dark);color:var(--white);text-align:center;padding:0 36px}
.svc svg{display:block;margin:20px auto 0}
.svc h3{font-size:18.5px;font-weight:700;line-height:23px;margin-top:10px;letter-spacing:.3px}
.svc p{font-size:16px;line-height:19.5px;margin-top:16px;text-align:justify;text-align-last:center}
.dots{position:absolute;left:0;width:1200px;display:flex;justify-content:center;gap:9px}
.dots span{width:34px;height:4px;background:var(--white)}
.services .dots span:first-child{background:var(--ink)}

/* work */
.work{top:2040px;height:611px;overflow:hidden}
.work-photo{position:absolute;inset:0;background:linear-gradient(90deg,#d9cdbd 0%,#e0d6cb 25%,#c7c4bd 45%,#e8ebe2 70%,#f4f4ef 100%)}
.work .card{left:431px;top:72px;width:693px;height:479px;padding:0 42px}
.work h2{margin-top:45px}
.work p{margin-top:16px;text-align:justify}

/* testimonials */
.reviews{top:2651px;height:721px;background:var(--dark)}
.reviews .section-title{top:70px;color:var(--white)}
.quote{position:absolute;top:225px}
.quote-mark{position:absolute;left:0;top:0}
.quote p{position:absolute;left:44px;top:48px;width:263px;color:#e6e6e6;font-size:18px;line-height:30.4px;text-align:justify}
.quote .name{position:absolute;left:44px;top:346px;color:var(--red);font-weight:700;font-size:18px;white-space:nowrap}
.reviews .dots{top:663px}
.reviews .dots span:first-child{background:var(--red)}

/* footer */
.footer{top:3372px;height:443px;background:var(--white)}
.footer h4{position:absolute;top:92px;color:var(--red);font-weight:700;font-size:22px;letter-spacing:.5px}
.links{position:absolute;left:95px;top:156px;list-style:none;font-size:19px;line-height:30.5px;color:var(--ink)}
.social{position:absolute;left:93px;top:298px;display:flex;gap:15px}
.social span{width:34px;height:34px;border:2px solid var(--red);border-radius:50%}
.contact{position:absolute;left:442px;top:156px;font-size:17px;line-height:30.5px;color:var(--ink)}
.contact .lbl{color:var(--red)}
.legal{position:absolute;left:857px;top:116px;font-size:16px;font-weight:700;line-height:20px;color:var(--ink)}
.legal .lbl{color:var(--red)}
.badge{position:absolute;left:836px}
.bar{top:3815px;height:54px;background:var(--footer-bar);color:#888;font-size:13px;display:flex;align-items:center;justify-content:center}
</style>
</head>
<body>

<header class="hero">
  <div class="hero-photo" role="img" aria-label="Foto: weißer Kastensprinter auf einer Landstraße in der Dämmerung"></div>
  <div class="hero-shade"></div>
  <div class="brand"><span class="brand-mark"></span>WELMACOR</div>
  <nav class="nav"><a href="#">STARTSEITE</a><a href="#">ÜBER UNS</a><a href="#">LEISTUNGEN</a><a href="#">KONTAKT</a></nav>
  <h1 class="hero-title">WELMACOR</h1>
  <div class="hero-sub">TRANSPORT | SPEDITION</div>
  <div class="hero-tag">Zuverlässigkeit und Vertrauen sind unsere Konstante</div>
  <div class="hero-btn">SEHR GERNE!</div>
</header>

<section class="about">
  <div class="about-photo" role="img" aria-label="Foto: weißer Kofferaufbau-Transporter vor einem Gebäude"></div>
  <div class="card">
    <h2>ÜBER UNS</h2>
    <p>Als gewissenhaftes Inhabergeführtes Unternehmen konzentrieren wir uns auf das machbare.Zuverlässigkeit und Vertrauen sind unsere Konstante. Wir sind stolz darauf, bereits jetzt zurückblickend sagen zu können: „Es hat sich gelohnt!“</p>
    <p>Unsere Zahlen, sowie der gesunde Wachstum sprechen für uns. Wir haben uns innerhalb kürzester Zeit von einem lokalen Spediteur zu einem Europaweit agierenden In-Time Logistikdienstleister entwickelt. Wir sind für alle Herausforderungen offen und lösen auch unmögliche Aufgaben. Hierbei spielt es keine Rolle ob es sich um Einzelaufträge oder Festtouren handelt. Unser Angebot orientiert sich immer an den Bedürfnissen und Erwartungen unser Kunden.Wir versprechen nichts, was wir nicht halten können!</p>
  </div>
</section>

<section class="services">
  <h2 class="section-title">ÜBERSICHT UNSERER<br>DIENSTLEISTUNGEN</h2>
  <div class="svc" style="left:92px">
    <svg width="64" height="64" viewBox="0 0 64 64" fill="none" stroke="#fff" stroke-width="2"><circle cx="32" cy="32" r="30"/><ellipse cx="32" cy="32" rx="13" ry="30"/><line x1="32" y1="2" x2="32" y2="62"/><line x1="2" y1="32" x2="62" y2="32"/><path d="M7 17h50M7 47h50"/></svg>
    <h3>DIREKT- UND<br>EXPRESSTRANSPORTE</h3>
    <p>Wir liefern schnell, flexibel und direkt – das heißt ohne Bei- und Umladung. Ihre zeitkritische Sendung übernehmen wir Bundesweit innerhalb von 60 Minuten.</p>
  </div>
  <div class="svc" style="left:446px">
    <svg width="88" height="64" viewBox="0 0 88 64" fill="none" stroke="#fff" stroke-width="2.5"><rect x="3" y="10" width="52" height="36" rx="2"/><path d="M55 20h16l12 14v12H55z"/><circle cx="20" cy="50" r="7" fill="var(--red-dark)"/><circle cx="68" cy="50" r="7" fill="var(--red-dark)"/></svg>
    <h3 style="margin-top:24px">PROJEKTLOGISTIK</h3>
    <p style="margin-top:24px">Just-in-Time für einen begrenzten Zeitraum? Gerne! Europaweit wickeln wir projektbezogene Transport- und Logistikaufgaben ab.</p>
  </div>
  <div class="svc" style="left:805px">
    <svg width="72" height="64" viewBox="0 0 72 64" fill="none" stroke="#fff" stroke-width="2.5"><path d="M20 62s-14-14-14-26a14 14 0 0 1 28 0c0 12-14 26-14 26z"/><circle cx="20" cy="36" r="5"/><path d="M56 28s-10-10-10-18a10 10 0 0 1 20 0c0 8-10 18-10 18z"/><circle cx="56" cy="10" r="3.5"/><path d="M28 58c10-2 16-10 24-24" stroke-dasharray="3 4"/></svg>
    <h3>REGEL UND<br>FESTTOUREN</h3>
    <p>Sie haben regelmäßig Fahrten zu einem bestimmten Empfänger? Wir übernehmen Ihre Ware zu einem fest vereinbarten Abholtermin und stellen diese je nach Vereinbarung direkt zu.</p>
  </div>
  <div class="dots" style="top:576px"><span></span><span></span></div>
</section>

<section class="work">
  <div class="work-photo" role="img" aria-label="Foto: Fahrerin in roter Kleidung am Steuer eines Transporters"></div>
  <div class="card">
    <h2>WIE WIR ARBEITEN</h2>
    <p>Wir sind uns darüber bewusst: Zeit ist Geld!<br>Und gerade in dem Bereich der In-Time Logistik gilt diese Redewendung doppelt.</p>
    <p style="margin-top:26px">Im Zentrum unserer Tätigkeit stehen Fahrzeuge mit einer Ladekapazität bis zu 12 Europaletten und einer Zuladung bis 1350 KG. Unser Fokus liegt auf zeitkritischer sowie sensibler Ware.Wir starten direkt nach Beladung, und je Transport übernehmen wir ausschließlich Ihre Ware - so verlieren wir keine wertvolle Zeit und das Risiko einer Beschädigung wird minimiert. Ihnen steht dabei immer das volle Fahrzeug zur Verfügung!Fahrerdaten.</p>
  </div>
</section>

<section class="reviews">
  <h2 class="section-title">WAS UNSERE<br>KUNDEN ÜBER UNS SAGEN</h2>
  <div class="quote" style="left:93px">
    <svg class="quote-mark" width="42" height="24" viewBox="0 0 42 24" fill="var(--red)"><path d="M0 0h17v13l-6 11H4l4-10H0z"/><path d="M23 0h17v13l-6 11h-7l4-10h-8z"/></svg>
    <p>Lorem ipsum dolor sit amet, consectetur adipiscing elit, sed do eiusmod tempor incididunt ut labore et dolore magna aliqua. Ut enim ad minim veniam, quis nostrud exercitation ullamco laboris nisi ut aliquip ex ea commodo consequat.</p>
    <div class="name">Jonas Kerber</div>
  </div>
  <div class="quote" style="left:446px">
    <svg class="quote-mark" width="42" height="24" viewBox="0 0 42 24" fill="var(--red)"><path d="M0 0h17v13l-6 11H4l4-10H0z"/><path d="M23 0h17v13l-6 11h-7l4-10h-8z"/></svg>
    <p style="left:50px">Lorem ipsum dolor sit amet, consectetur adipiscing elit, sed do eiusmod tempor incididunt ut labore et dolore magna aliqua. Ut enim ad minim veniam, quis nostrud exercitation ullamco laboris nisi ut aliquip ex ea commodo consequat.</p>
    <div class="name" style="left:50px">Jonas Kerber</div>
  </div>
  <div class="quote" style="left:813px">
    <svg class="quote-mark" width="42" height="24" viewBox="0 0 42 24" fill="var(--red)"><path d="M0 0h17v13l-6 11H4l4-10H0z"/><path d="M23 0h17v13l-6 11h-7l4-10h-8z"/></svg>
    <p style="left:49px">Lorem ipsum dolor sit amet, consectetur adipiscing elit, sed do eiusmod tempor incididunt ut labore et dolore magna aliqua. Ut enim ad minim veniam, quis nostrud exercitation ullamco laboris nisi ut aliquip ex ea commodo consequat.</p>
    <div class="name" style="left:49px">Jonas Kerber</div>
  </div>
  <div class="dots"><span></span><span></span></div>
</section>

<footer class="footer">
  <h4 style="left:93px">QUICKLINKS</h4>
  <ul class="links"><li>Startseite</li><li>AGB</li><li>Impressum</li><li>Datenschutz</li></ul>
  <div class="social"><span></span><span></span><span></span></div>
  <h4 style="left:442px">KONTAKTINFORMATION</h4>
  <div class="contact">
    WELMACOR e.K.<br>Lindenweg 14<br>37999 Falkenrode<br><br>
    <span class="lbl">Tel.:</span> +49 (0) 5500 12345 -10<br>
    <span class="lbl">Fax:</span> +49 (0) 5500 12345 -190<br>
    <span class="lbl">Mail:</span> kontakt@welmacor-logistik.example
  </div>
  <div class="legal">
    <span class="lbl">Registergericht:</span> Falkenrode<br>
    <span class="lbl">Registernummer:</span> HRA 400123<br><br>
    <span class="lbl">Finanzamt:</span> Falkenrode<br>
    <span class="lbl">Umsatzsteuer-ID:</span> DE 000111222
  </div>
  <div class="badge" style="top:300px;width:276px;height:46px;border-radius:6px;background:#dfe3ea"></div>
  <div class="badge" style="top:372px;left:855px;width:182px;height:34px;border-radius:4px;background:#d9d9d9"></div>
</footer>

<div class="bar" style="position:absolute;left:0;width:1200px">© 2020 - Copyright WELMACOR e.K - Alle Rechte vorbehalten.</div>

</body>
</html>
```